Lettershop sucht Design
Gerne wieder! als wir Quento´s Design sahen, wussten wir schon, dass es genau dieses sein wird!! Er machte uns gute Vorschläge zwecks Positionierung und Inhalte. Das ganze Brivalto-Team ist sehr zufrieden und wir können Ihn zu 100% Weiterempfehlen. Vielen Dank!! When Quento came up with his designs we just thought: "That's it". I can only imagine how hard it must be to understand the needs of a client without knowing him/her personally. But he got it all right. If you need a professional, reliable designer then he is the right choice, 100%. Thank you :-) Best regards, Brivaltoplanet-Team
Zielgruppe
Lettershop
Zielgruppe Firmen
Aufgabenstellung
Ansprechenderes Design für unsere kleine Seite
http://www.briefdienst-beispiel.de/

```html
<!DOCTYPE html>
<html lang="de">
<head>
<meta charset="utf-8">
<title>Lettershop Stuttgart – Post die ankommt</title>
<link rel="stylesheet" href="https://fonts.googleapis.com/css2?family=Open+Sans:wght@300;400;600;700&display=swap">
<style>
:root{
  --blue:#4a75ba;
  --blue-dark:#24528f;
  --teal:#88b6c1;
  --green:#86cba1;
  --grey-bar:#e8e8e8;
  --text:#555;
  --text-dark:#222;
  --white:#fff;
  --input:#e6e6e6;
}
*{box-sizing:border-box;margin:0;padding:0}
html,body{width:1037px;height:1200px;overflow:hidden}
body{font-family:"Open Sans",Arial,sans-serif;color:var(--text);background:var(--white);position:relative}
.abs{position:absolute}

.topbar{left:0;top:0;width:1037px;height:24px;background:var(--grey-bar)}
.topbar .welcome{left:176px;top:6px;font-size:8px;font-weight:300;color:#666}
.social{display:flex;gap:6px}
.social span{width:19px;height:19px;border-radius:50%;background:var(--blue);display:block}
.topbar .social{left:538px;top:3px}
.hotline{left:660px;top:0;width:194px;height:24px;background:var(--blue);color:var(--white);font-size:8px;display:flex;align-items:center;gap:6px;padding-left:9px}
.hotline b{font-weight:700;margin-right:6px}

.header{left:0;top:24px;width:1037px;height:78px;background:var(--white)}
.brand{left:174px;top:24px;font-size:17px;font-weight:600;color:var(--blue);letter-spacing:.5px}
.nav{left:492px;top:35px;display:flex;gap:25px;font-size:9.5px;color:var(--text-dark)}

.hero{left:0;top:102px;width:1037px;height:453px;background:linear-gradient(#4d78b9 0%,#8fbcd0 30%,#b3dacb 55%,#f4f2e0 100%)}
.hero h1{left:0;width:1037px;top:24px;text-align:center;font-size:28.5px;font-weight:700;color:var(--white);letter-spacing:.2px}
.art{border-radius:50%;background:rgba(255,255,255,.55)}
.art-left{left:66px;top:74px;width:248px;height:228px}
.art-mid{left:418px;top:125px;width:92px;height:100px}
.art-right{left:808px;top:45px;width:80px;height:95px}
.form-title{left:470px;width:320px;top:64px;text-align:right;line-height:1}
.form-title .t1{font-size:21px;font-weight:700;color:var(--blue-dark);display:block}
.form-title .t2{font-size:16.5px;font-weight:400;color:var(--blue-dark);display:block;margin-top:2px}
.field label{display:block;font-size:9px;color:var(--white);margin-left:9px;margin-bottom:2px}
.field .input{width:252px;height:36px;background:var(--white);padding:3px 4px}
.field .input span{display:block;height:30px;background:var(--input)}
.f1{left:541px;top:108px}.f2{left:541px;top:164px}.f3{left:541px;top:220px}
.consent{left:541px;top:285px;display:flex;gap:7px;font-size:10px;color:#555;width:260px;line-height:1.25}
.consent .box{width:17px;height:15px;background:var(--white);border:3px solid #e6e6e6;flex:none}
.cta{left:546px;top:321px;width:243px;height:49px;border-radius:3px;background:linear-gradient(#5a86c5,#4468ad);color:var(--white);font-size:16.5px;font-weight:700;display:flex;align-items:center;justify-content:center}
.note{left:553px;top:381px;width:236px;font-size:8px;line-height:12.5px;color:#555;hyphens:auto;-webkit-hyphens:auto}

.intro{left:0;top:555px;width:1037px;height:136px;background:linear-gradient(#fff 55%,#ececec 100%);text-align:center}
.intro h2{margin-top:46px;font-size:21.5px;font-weight:700;color:var(--blue)}
.intro p{font-size:12.5px;color:#666;margin-top:1px}

.card{top:726px;height:322px;color:var(--white);text-align:center;padding:84px 11px 0;hyphens:auto;-webkit-hyphens:auto}
.card .fold-a,.card .fold-b{position:absolute;left:0;top:0;width:21px;height:26px}
.card .fold-a{background:var(--white);clip-path:polygon(0 0,100% 0,0 100%)}
.card .fold-b{background:rgba(255,255,255,.35);clip-path:polygon(100% 0,100% 100%,0 100%)}
.card h3{font-size:12.5px;font-weight:600;line-height:17px;margin-bottom:11px}
.card p{font-size:9.8px;font-weight:300;line-height:16.6px}
.card .btn{position:absolute;top:260px;height:40px;border:1px solid var(--white);border-radius:2px;display:flex;align-items:center;justify-content:center;gap:6px;font-size:9.5px;font-weight:700;hyphens:none}
.c1{left:162px;width:159px;background:var(--blue)}
.c2{left:335px;width:159px;background:var(--teal)}
.c3{left:508px;width:345px;background:var(--green);padding:84px 26px 0}
.c1 .btn,.c2 .btn{left:25px;width:109px}
.c3 .btn{left:25px;width:296px;font-size:12.5px}

.footer{left:0;top:1048px;width:1037px;height:152px;background:linear-gradient(#fff 60%,#ececec);text-align:center;font-size:9.5px;color:#555}
.footer .co{margin-top:26px;font-weight:700}
.footer .tel{margin-top:6px}
.footer .mail{margin-top:3px;color:var(--blue)}
.footer .social{justify-content:center;margin-top:10px}
.footer .links{margin-top:8px;font-size:8.5px}
</style>
</head>
<body>
<div class="topbar abs">
  <div class="welcome abs">Willkommen zum Lettershop Stuttgart</div>
  <div class="social abs"><span></span><span></span><span></span><span></span><span></span></div>
  <div class="hotline abs"><b>SOFORTBERATUNG:</b>
    <svg width="11" height="11" viewBox="0 0 24 24"><path fill="#fff" d="M6.6 10.8a15 15 0 0 0 6.6 6.6l2.2-2.2a1 1 0 0 1 1-.25 11.4 11.4 0 0 0 3.6.57 1 1 0 0 1 1 1V20a1 1 0 0 1-1 1A17 17 0 0 1 3 4a1 1 0 0 1 1-1h3.5a1 1 0 0 1 1 1c0 1.25.2 2.45.57 3.57a1 1 0 0 1-.25 1z"/></svg>
    (0711) 55 01 23 45</div>
</div>

<header class="header abs">
  <div class="brand abs">Brivalto Versand</div>
  <nav class="nav abs"><span>HOME</span><span>LETTERSHOP STUTTGART</span><span>LEISTUNGEN</span><span>KONTAKT</span></nav>
</header>

<section class="hero abs">
  <div class="art art-left abs" role="img" aria-label="Weiße Taube mit Briefumschlag zwischen Wolken"></div>
  <div class="art art-mid abs" role="img" aria-label="Fliegende weiße Taube"></div>
  <div class="art art-right abs" role="img" aria-label="Fliegende weiße Taube"></div>
  <h1 class="abs">LETTERSHOP STUTTGART - POST DIE ANKOMMT</h1>
  <div class="form-title abs"><span class="t1">GRATIS LETTERSHOP-GUIDE</span><span class="t2">JETZT NEWSLETTER ABONNIEREN:</span></div>
  <div class="field f1 abs"><label>VORNAME: *</label><div class="input"><span></span></div></div>
  <div class="field f2 abs"><label>NACHNAME: *</label><div class="input"><span></span></div></div>
  <div class="field f3 abs"><label>E-Mail Adresse: *</label><div class="input"><span></span></div></div>
  <div class="consent abs"><span class="box"></span><span>Ich habe die Datenschutzrichtlinien gelesen und bestätige diese hiermit.</span></div>
  <div class="cta abs">JETZT ABONNIEREN</div>
  <p class="note abs">Sie erhalten zukünftig in unregelmäßigen Abständen, maxi&shy;mal einmal pro Monat aktuelle Informationen in Form eines Newsletters. Ihre Daten werden NICHT an Dritte weitergegeben!</p>
</section>

<section class="intro abs">
  <h2>ABONNIEREN SIE UNSEREN NEWSLETTER</h2>
  <p>UND SIE ERHALTEN DEN GRATIS LETTERSHOP-GUIDE MIT WEITGEHENDEN INFORMATIONEN PER E-MAIL.</p>
</section>

<article class="card c1 abs">
  <span class="fold-a"></span><span class="fold-b"></span>
  <h3>LETTERSHOP<br>EXPERTEN</h3>
  <p>Datenaufbereitung, Falzen, Portooptimierung, Kuvertieren, Folieren, Postaufliefern, Fulfill&shy;ment und vieles mehr.</p>
  <div class="btn">MEHR DAZU</div>
</article>
<article class="card c2 abs">
  <span class="fold-a"></span><span class="fold-b"></span>
  <h3>GÜNSTIG UND<br>SICHER</h3>
  <p>Wir arbeiten neben der Nationalpost AG auch erfol&shy;greich mit allen privaten Ver&shy;sanddienstleistern zusammen, um für jeden Ihrer Aufträge die beste Lösung zu finden.</p>
  <div class="btn">MEHR DAZU</div>
</article>
<article class="card c3 abs">
  <span class="fold-a"></span><span class="fold-b"></span>
  <h3>LETTERSHOP<br>PERFEKT</h3>
  <p>Ob kleine oder große Auflagen, Ihr täglicher Rechnungsversand oder der große Aussand Ihres Quartalskatalogs, Ihr Mailing- oder Ihr Zeitschriftenversand. Kuvertiert, foliert, mit oder ohne Beila&shy;gen - wir finden immer die perfekte Lösung für Sie.<br><br>Fragen Sie Ihre nächste Aufgabe einfach gleich bei uns an.</p>
  <div class="btn"><svg width="13" height="13" viewBox="0 0 24 24"><path fill="#fff" d="M6.6 10.8a15 15 0 0 0 6.6 6.6l2.2-2.2a1 1 0 0 1 1-.25 11.4 11.4 0 0 0 3.6.57 1 1 0 0 1 1 1V20a1 1 0 0 1-1 1A17 17 0 0 1 3 4a1 1 0 0 1 1-1h3.5a1 1 0 0 1 1 1c0 1.25.2 2.45.57 3.57a1 1 0 0 1-.25 1z"/></svg>TEL.: (0711) 55 01 23 45</div>
</article>

<footer class="footer abs">
  <div class="co">BRIVALTO VERSAND GMBH</div>
  <div class="tel">TEL.: (0711) 55 01 23 45</div>
  <div class="mail">KONTAKT@BRIVALTO-VERSAND.DE</div>
  <div class="social"><span></span><span></span><span></span><span></span><span></span></div>
  <div class="links">DATENSCHUTZ &nbsp;|&nbsp; IMPRESSUM</div>
</footer>
</body>
</html>
```